Small company security and risk consulting startup needs an explosive message via marketing colla...

Need a two page (front/back) flyer that calls out our three primary service areas incorporating tallyquill developed logo and website visuals. Something that grabs attention at first glance to entice the viewer to read and connect for a services consultation. I will need the ability to make minor adjustments and add language.

```html
<!DOCTYPE html>
<html lang="en">
<head>
<meta charset="utf-8">
<title>Ardent Shield Consulting Services – Flyer Front and Back</title>
<link href="https://fonts.googleapis.com/css2?family=Anton&family=Oswald:wght@500;600&family=Lato:wght@400;700;900&display=swap" rel="stylesheet">
<style>
  :root {
    --stage: #8c8c8c;
    --navy: #0f2a3a;
    --navy-deep: #0a1820;
    --signal-red: #e8202a;
    --wine: #5a1418;
    --ember: #8e1d22;
    --white: #ffffff;
    --body-grey: #c9d1d6;
    --highlight: #ffe81a;
  }
  * { box-sizing: border-box; margin: 0; padding: 0; }
  html, body { width: 1200px; height: 900px; overflow: hidden; background: var(--stage); }
  body { position: relative; font-family: "Lato", sans-serif; }

  .page {
    position: absolute;
    top: 153px;
    width: 420px;
    height: 594px;
    overflow: hidden;
    box-shadow: 0 18px 40px rgba(0,0,0,.35);
  }
  .page--front { left: 150px; background: var(--navy-deep); }
  .page--back { left: 630px; background: var(--wine); }
  .page svg.page-art { position: absolute; inset: 0; width: 100%; height: 100%; }

  /* Front: headline */
  .headline {
    position: absolute; top: 44px; left: 196px; width: 210px;
    font-family: "Anton", sans-serif; color: var(--white);
    line-height: .95; text-transform: uppercase;
  }
  .headline__line { display: block; font-size: 44px; letter-spacing: 1px; }
  .headline__sub {
    display: block; margin-top: 6px;
    font-family: "Lato", sans-serif; font-weight: 900;
    font-size: 14px; color: var(--highlight); letter-spacing: .5px;
  }

  /* Front: brand block */
  .brand {
    position: absolute; top: 196px; left: 70px; width: 230px;
    text-align: center; color: var(--white);
  }
  .brand__row { display: flex; align-items: center; justify-content: center; gap: 7px; }
  .brand__square { width: 16px; height: 16px; background: var(--signal-red); }
  .brand__name { font-weight: 900; font-size: 19px; color: var(--white); }
  .brand__descriptor { font-size: 7.5px; letter-spacing: 3px; margin-top: 3px; }
  .brand__values { font-size: 6px; letter-spacing: 1.5px; color: var(--signal-red); margin-top: 3px; }

  /* Front: text columns (kept clear of the service icons) */
  .info-block { position: absolute; left: 28px; width: 156px; color: var(--white); }
  .info-block--about { top: 336px; }
  .info-block--why { top: 462px; }
  .info-block__title {
    font-weight: 900; font-size: 19px; text-transform: uppercase;
    display: inline-block; padding-bottom: 3px; border-bottom: 2px solid var(--signal-red);
  }
  .info-block__text { font-size: 6.6px; line-height: 1.45; color: var(--body-grey); margin-top: 6px; }

  /* Front: services */
  .service { position: absolute; left: 254px; width: 156px; color: var(--white); }
  .service--security { top: 316px; }
  .service--risk { top: 386px; }
  .service--consulting { top: 462px; }
  .service__title {
    font-family: "Oswald", sans-serif; font-weight: 600; font-size: 15px;
    line-height: 1.05; text-transform: uppercase;
  }
  .service__text { font-size: 6.2px; line-height: 1.4; margin-top: 3px; }

  /* Back: contact band */
  .contact { position: absolute; left: 26px; bottom: 22px; color: var(--white); }
  .contact__title {
    font-weight: 900; font-size: 21px; color: var(--highlight);
    text-transform: uppercase; margin-bottom: 6px;
  }
  .contact__line { display: flex; align-items: center; gap: 9px; font-size: 13px; margin-top: 3px; }
  .contact__line svg { width: 12px; height: 12px; flex: none; }
  .follow { position: absolute; right: 22px; bottom: 86px; color: var(--white); text-align: center; }
  .follow__label { font-size: 8px; font-weight: 700; text-transform: uppercase; }
  .follow__dots { display: flex; gap: 5px; justify-content: center; margin-top: 3px; }
  .follow__dots span { width: 9px; height: 9px; border-radius: 50%; background: var(--white); }
</style>
</head>
<body>

<!-- FRONT -->
<section class="page page--front" aria-label="Flyer front">
  <svg class="page-art" viewBox="0 0 420 594">
    <defs>
      <radialGradient id="heroGlow" cx="0.4" cy="0.5" r="0.75">
        <stop offset="0" stop-color="#b2242b"/>
        <stop offset="0.55" stop-color="#6b1a1f"/>
        <stop offset="1" stop-color="#2a0d10"/>
      </radialGradient>
    </defs>
    <rect class="hero-photo" x="0" y="0" width="420" height="300" fill="url(#heroGlow)"
          role="img" aria-label="Close-up photo of an eye overlaid with a red digital targeting interface"/>
    <path class="navy-wave" d="M0 190 Q210 155 420 205 L420 594 L0 594 Z" fill="var(--navy)"/>
    <path class="deep-wave" d="M0 300 Q220 345 420 290 L420 594 L0 594 Z" fill="var(--navy-deep)"/>
    <path class="service-panel" d="M266 262 L420 262 L420 540 L266 540 Q209 400 266 262 Z" fill="var(--signal-red)"/>
    <path class="footer-strip" d="M0 560 Q210 530 420 540 L420 594 L0 594 Z" fill="var(--navy-deep)"/>

    <g class="service-icon" transform="translate(230 338)">
      <circle r="23" fill="var(--white)" stroke="var(--navy-deep)" stroke-width="3"/>
      <rect x="-12" y="-9" width="24" height="15" rx="1.5" fill="none" stroke="#1b1b1b" stroke-width="1.8"/>
      <path d="M-4 10 L4 10 M0 6 L0 10" stroke="#1b1b1b" stroke-width="1.8"/>
      <circle cx="0" cy="-1.5" r="3" fill="#1b1b1b"/>
    </g>
    <g class="service-icon" transform="translate(220 410)">
      <circle r="23" fill="var(--white)" stroke="var(--navy-deep)" stroke-width="3"/>
      <circle r="7" fill="none" stroke="#1b1b1b" stroke-width="1.8"/>
      <circle r="2.5" fill="#1b1b1b"/>
      <path d="M0 -12 V-8 M0 8 V12 M-12 0 H-8 M8 0 H12 M-8.5 -8.5 L-5.7 -5.7 M5.7 5.7 L8.5 8.5 M8.5 -8.5 L5.7 -5.7 M-5.7 5.7 L-8.5 8.5" stroke="#1b1b1b" stroke-width="1.8"/>
    </g>
    <g class="service-icon" transform="translate(232 484)">
      <circle r="23" fill="var(--white)" stroke="var(--navy-deep)" stroke-width="3"/>
      <path d="M-6 4 Q-11 -1 -9 -7 Q-6 -13 0 -13 Q6 -13 9 -7 Q11 -1 6 4 L6 8 L-6 8 Z" fill="none" stroke="#1b1b1b" stroke-width="1.8"/>
      <path d="M-4 11 H4 M-3 14 H3" stroke="#1b1b1b" stroke-width="1.8"/>
    </g>
  </svg>

  <h1 class="headline">
    <span class="headline__line">Ardent</span>
    <span class="headline__line">Shield</span>
    <span class="headline__sub">Consulting Services</span>
  </h1>

  <div class="brand">
    <div class="brand__row"><span class="brand__square"></span><span class="brand__name">ArdentShield</span></div>
    <div class="brand__descriptor">CONSULTING SERVICES</div>
    <div class="brand__values">commitment · integrity · results</div>
  </div>

  <div class="info-block info-block--about">
    <h2 class="info-block__title">About Us</h2>
    <p class="info-block__text">Lorem ipsum dolor sit amet, consectetuer adipiscing elit, sed diam nonummy nibh euismod tincidunt ut laoreet dolore magna aliquam erat volutpat. Ut wisi enim ad minim veniam, quis nostrud exerci tation ullamcorper suscipit lobortis nisl ut aliquip ex ea commodo consequat. Duis autem vel eum iriure dolor in hendrerit in vulputate velit esse molestie consequat.</p>
  </div>

  <div class="info-block info-block--why">
    <h2 class="info-block__title">Why We Are</h2>
    <p class="info-block__text">Lorem ipsum dolor sit amet, consectetuer adipiscing elit, sed diam nonummy nibh euismod tincidunt ut laoreet dolore magna aliquam erat volutpat. Ut wisi enim ad minim veniam, quis nostrud exerci tation ullamcorper suscipit lobortis nisl ut aliquip ex ea commodo consequat. Duis autem vel eum iriure dolor.</p>
  </div>

  <div class="service service--security">
    <h3 class="service__title">Natinal Security</h3>
    <p class="service__text">Lorem ipsum dolor sit amet, consectetuer adipiscing elit, sed diam nonummy nibh euismod tincidunt ut laoreet dolore magna aliquam erat</p>
  </div>
  <div class="service service--risk">
    <h3 class="service__title">Risk Management<br>Services</h3>
    <p class="service__text">Lorem ipsum dolor sit amet, consectetuer adipiscing elit, sed diam nonummy nibh euismod tincidunt ut laoreet dolore magna aliquam erat</p>
  </div>
  <div class="service service--consulting">
    <h3 class="service__title">Consulting Services</h3>
    <p class="service__text">Lorem ipsum dolor sit amet, consectetuer adipiscing elit, sed diam nonummy nibh euismod tincidunt ut laoreet dolore magna aliquam erat</p>
  </div>
</section>

<!-- BACK -->
<section class="page page--back" aria-label="Flyer back">
  <svg class="page-art" viewBox="0 0 420 594">
    <defs>
      <linearGradient id="monitorRoom" x1="0" y1="0" x2="1" y2="1">
        <stop offset="0" stop-color="#c8202a"/>
        <stop offset="0.45" stop-color="#8e1d22"/>
        <stop offset="1" stop-color="#3a0f12"/>
      </linearGradient>
    </defs>
    <rect class="operator-photo" x="0" y="0" width="420" height="594" fill="url(#monitorRoom)"
          role="img" aria-label="Red-tinted photo of a security operator at a desk watching a wall of surveillance monitors"/>
    <path class="contact-band" d="M0 500 L420 470 L420 594 L0 594 Z" fill="var(--navy)"/>
  </svg>

  <div class="follow">
    <div class="follow__label">Follow Us</div>
    <div class="follow__dots"><span></span><span></span><span></span></div>
  </div>

  <div class="contact">
    <h2 class="contact__title">Get In Touch</h2>
    <p class="contact__line">
      <svg viewBox="0 0 12 12"><path d="M6 0.5 A4 4 0 0 1 10 4.5 C10 7.5 6 11.5 6 11.5 C6 11.5 2 7.5 2 4.5 A4 4 0 0 1 6 0.5 Z" fill="#fff"/><circle cx="6" cy="4.5" r="1.5" fill="var(--navy)"/></svg>
      482 Harlow Ridge Ave Suite 12 Austin TX 78701
    </p>
    <p class="contact__line">
      <svg viewBox="0 0 12 12"><path d="M2.5 1 L4.5 1 L5.5 3.8 L4.2 4.8 Q5.2 7 7.2 7.8 L8.2 6.5 L11 7.5 L11 9.5 Q10.5 11 9 11 Q1 10 1 2.5 Q1 1 2.5 1 Z" fill="#fff"/></svg>
      (555) 014 7730
    </p>
    <p class="contact__line">
      <svg viewBox="0 0 12 12"><rect x="0.5" y="2" width="11" height="8" fill="#fff"/><path d="M0.5 2 L6 6.5 L11.5 2" fill="none" stroke="var(--navy)" stroke-width="1"/></svg>
      info@ardentshield.example
    </p>
  </div>
</section>

</body>
</html>
```